Modern & Fresh Sumeray Book Cover

Need a creative e-book cover for my book.

Title: Get Sumeray Sorted
Subtitle: Learn How To Easily Choose & Enroll in the Perfect Coverage at the Perfect Time.

Target Market(s)

60-70 year olds in the United States

Font styles to use
Sans Serif

Colors
9bcb3c
33a6d7

Requirements
Must have
• Must look modern and fresh.
• Use our company colors www.BrovaMint.com

```html
<!DOCTYPE html>
<html lang="en">
<head>
<meta charset="utf-8">
<title>Get Sumeray Sorted – Book Cover</title>
<link rel="stylesheet" href="https://fonts.googleapis.com/css2?family=Anton&family=Roboto+Condensed:wght@300&display=swap">
<style>
  :root {
    --page: #ffffff;
    --cover: #ffffff;
    --copy-grey: #d6d6d6;
    --pill-red: #e5432f;
    --pill-green: #98c35d;
    --pill-blue: #0097d9;
    --white: #ffffff;
  }
  * { box-sizing: border-box; margin: 0; padding: 0; }
  html, body {
    width: 1175px;
    height: 1200px;
    overflow: hidden;
    background: var(--page);
  }
  .cover {
    position: absolute;
    left: 244px;
    top: 119px;
    width: 679px;
    height: 946px;
    background: var(--cover);
    overflow: hidden;
  }
  .backdrop-copy {
    position: absolute;
    left: -8px;
    top: -10px;
    width: 700px;
    font-family: Arial, Helvetica, sans-serif;
    font-size: 21px;
    line-height: 21.3px;
    color: var(--copy-grey);
  }
  .shapes {
    position: absolute;
    left: 0;
    top: 0;
    width: 679px;
    height: 946px;
  }
  .figures {
    position: absolute;
    left: 34px;
    top: 638px;
    width: 241px;
    height: 303px;
    background: linear-gradient(180deg, rgba(239,239,239,0.5), rgba(226,226,226,0.6));
  }
  .title {
    position: absolute;
    left: 330px;
    top: 291px;
    font-family: "Anton", Impact, sans-serif;
    font-weight: 400;
    font-size: 73px;
    line-height: 68px;
    color: var(--white);
    text-transform: uppercase;
    letter-spacing: -0.5px;
  }
  .title span { display: block; height: 68px; }
  .subtitle {
    position: absolute;
    right: 55px;
    top: 528px;
    width: 300px;
    font-family: "Roboto Condensed", "Arial Narrow", sans-serif;
    font-weight: 300;
    font-size: 31px;
    line-height: 34px;
    color: var(--white);
    text-align: right;
  }
  .subtitle span { display: block; white-space: nowrap; }
</style>
</head>
<body>
  <div class="cover">
    <p class="backdrop-copy">
      If you are confused by Sumeray (don't worry, most people are), then we urge you to attend one of BrovaMint's incredibly useful and informative Mastering Sumeray Workshops! We offer these entirely free, non-sales pitch, and helpful Sumeray resources in Riverton because we understand how confusing navigating the complex Sumeray maze can be, and we want to help you make the best decision for your golden years. When you come to one of BrovaMint's Sumeray educational workshops and utilize our helpful Sumeray resources in Riverton, you will learn all about how Sumeray works. Our expert Sumeray teacher, Delbert, will clearly explain all your options. In just two informative hours, you will know when to enroll in Sumeray, what Sumeray A-B-C-D consists of, how to select the right drug plan, how to avoid the "donut hole," and much more! We'll also have a chance to hear and answer any additional questions you have. If you are confused by Sumeray (don't worry, most people are), then we urge you to attend one of BrovaMint's incredibly useful and informative Mastering Sumeray Workshops! We offer these entirely free, non-sales pitch, and helpful Sumeray resources in Riverton because we understand how confusing navigating the complex Sumeray maze can be, and we want to help you make the best decision for your golden years. When you come to one of BrovaMint's Sumeray educational workshops and utilize our helpful Sumeray resources in Riverton, you will learn all about how Sumeray works. Our expert Sumeray teacher, Delbert, will clearly explain all your options. In just two informative hours, you will know when to enroll in Sumeray, what Sumeray A-B-C-D consists of, how to select the right drug plan, how to avoid the "donut hole," and much more! We'll also have a chance to hear and answer any additional questions you have. If you are confused by Sumeray (don't worry, most people are), then we urge you to attend one of BrovaMint's incredibly useful and informative Mastering Sumeray Workshops! We offer these entirely free, non-sales pitch, and helpful Sumeray resources in Riverton because we understand how confusing navigating the complex Sumeray maze can be, and we want to help you make the best decision for your golden years. When you come to one of BrovaMint's Sumeray educational workshops and utilize our helpful Sumeray resources in Riverton, you will learn all about how Sumeray works. Our expert Sumeray teacher, Delbert, will clearly explain all your options. In just two informative hours, you will know when to enroll in Sumeray, what Sumeray A-B-C-D consists of, how to select the right drug plan, how to avoid the "donut hole," and much more! We'll also have a chance to hear and answer any additional questions you have.
    </p>

    <div class="figures" role="img" aria-label="Line drawing of an older couple walking together, the man with a cane"></div>

    <svg class="shapes" viewBox="0 0 679 946" aria-hidden="true">
      <circle class="pill-red" cx="198" cy="24" r="163" fill="var(--pill-red)"/>
      <rect x="235" y="57" width="81" height="20" fill="var(--white)"/>
      <rect x="265" y="27" width="20" height="81" fill="var(--white)"/>
      <path class="pill-green" d="M313 506 V266.5 A163.5 163.5 0 0 1 640 266.5 V506 Z" fill="var(--pill-green)"/>
      <path class="pill-blue" d="M313 516 H640 V754.5 A163.5 163.5 0 0 1 313 754.5 Z" fill="var(--pill-blue)"/>
    </svg>

    <h1 class="title">
      <span>Get</span>
      <span>Sumeray</span>
      <span>Sorted</span>
    </h1>

    <p class="subtitle">
      <span>Learn How To Easily</span>
      <span>Choose &amp; Enroll</span>
      <span>in the Perfect Coverage</span>
      <span>at the Perfect Time</span>
    </p>
  </div>
</body>
</html>
```